Real State Agency App

We need an app design for a real state agency, we provide mockups for our project that ilustrates very well what we need
our web site is www.brindlevaleestates.com,

Target Market(s)

Tourism

Font styles to use
Other font styles liked:
• attached you will find it

Requirements
Must have
• Colors like the logo

```html
<!DOCTYPE html>
<html lang="en">
<head>
<meta charset="utf-8">
<title>Brindlevale Estates – App Screens</title>
<link href="https://fonts.googleapis.com/css2?family=Source+Sans+3:wght@400;600;700&display=swap" rel="stylesheet">
<style>
:root{
  --stage:#bcbdbf;
  --teal:#1a9ac9;
  --gold:#e0b93a;
  --gold-line:#e8d9a2;
  --ink:#5d5d5d;
  --muted:#9a9a9a;
  --panel:#ececec;
  --white:#ffffff;
}
*{box-sizing:border-box;margin:0;padding:0}
html,body{width:1200px;height:994px;overflow:hidden}
body{background:var(--stage);font-family:"Source Sans 3",sans-serif;color:var(--ink);position:relative}
.screen{position:absolute;width:244px;height:430px;background:linear-gradient(#fff 0%,#fff 35%,#f1f1f1 100%);box-shadow:1px 2px 4px rgba(0,0,0,.35);overflow:hidden}
.screen>*{position:absolute}
.status{top:0;left:0;width:100%;height:20px}
.signal{position:absolute;left:7px;top:8px;display:flex;align-items:flex-end;gap:1px}
.signal i{display:block;width:2px;background:#b5b5b5}
.clock{position:absolute;left:0;right:0;top:4px;text-align:center;font-size:11px;color:#b5b5b5;font-weight:600}
.battery{position:absolute;right:7px;top:6px;font-size:6px;color:#b5b5b5;display:flex;align-items:center;gap:2px}
.battery b{display:block;width:16px;height:5px;background:#c3c3c3}
.menu{left:6px;top:26px;width:11px}
.menu i{display:block;height:1.6px;background:var(--teal);margin-bottom:2.4px}
.badge{left:92px;top:23px;width:60px;height:60px;border-radius:50%;background:#fff;border:2px solid #dcdcdc;box-shadow:0 2px 3px rgba(0,0,0,.15)}
.badge svg{position:absolute;left:14px;top:14px;width:28px;height:28px}
.heading{left:0;width:100%;text-align:center;font-size:9.5px;font-weight:600;color:var(--teal)}
.copy{font-size:6.6px;line-height:1.35;color:var(--ink);text-align:justify}
.field{height:18px;background:#fff;border:1px solid var(--gold-line);border-radius:2px;font-size:5.8px;color:var(--muted);padding:5px 0 0 7px;box-shadow:0 1px 1px rgba(0,0,0,.08)}
.select{height:18px;background:#fff;border:1px solid var(--gold-line);border-radius:2px;font-size:5.8px;color:var(--muted);padding:5px 0 0 7px}
.select .drop{position:absolute;right:0;top:0;width:19px;height:100%;background:var(--gold)}
.drop::after,.bar::after{content:"";position:absolute;right:6px;top:6px;border-left:4px solid transparent;border-right:4px solid transparent;border-top:4px solid #fff}
.bar{height:17px;background:var(--gold);border-radius:2px;font-size:5.8px;color:#fff;padding:5px 0 0 7px}
.area{background:#fff;border:1px solid var(--gold-line);border-top:none}
.area::after{content:"";position:absolute;right:3px;top:2px;width:2px;height:8px;background:#cfcfcf}
.btn{height:17px;background:var(--teal);border-radius:1px;color:#fff;font-size:8px;display:flex;align-items:center;justify-content:center;gap:7px;box-shadow:0 1px 2px rgba(0,0,0,.2)}
.btn svg{width:10px;height:10px}
.photo{background:linear-gradient(160deg,#dfeef8 0%,#f4f1e8 40%,#7ca44e 62%,#c79a72 80%,#5cc0e6 100%)}
.brandname{left:0;width:100%;text-align:center;font-size:17px;font-weight:700;color:#1d3f8f}
.brandname span{display:inline-block;width:7px;height:7px;border-radius:50%;background:var(--teal);margin-right:5px;vertical-align:middle}
.nav{left:53px;width:136px;height:25px;background:#fff;border-radius:2px;box-shadow:0 1px 2px rgba(0,0,0,.2);display:flex;align-items:center;font-size:6px;color:var(--ink)}
.nav .ico{width:32px;height:100%;border-right:1px solid #e2e2e2;display:flex;align-items:center;justify-content:center}
.nav .ico svg{width:14px;height:14px}
.nav .lbl{flex:1;text-align:center}
.nav.active{background:var(--teal);color:#fff}
.nav.active .ico{border-right-color:rgba(255,255,255,.35)}
.lang{top:401px;width:50px;height:11px;background:#fff;font-size:6px;display:flex;align-items:center;justify-content:center;color:var(--ink)}
.lang.on{background:var(--gold);color:#fff}
.result-photo{left:14px;width:73px;height:72px}
.result{left:98px;width:132px}
.result h4{font-size:7px;font-weight:400;color:var(--gold);margin-bottom:2px}
.result p{font-size:6.3px;line-height:1.3;color:var(--ink)}
.result a{font-size:7.2px;color:var(--teal);text-decoration:none}
.service{left:54px;width:134px;height:18px;background:#fff;border:1px solid var(--gold-line);border-radius:2px;font-size:6px;text-align:center;padding-top:5px;color:var(--ink);box-shadow:0 1px 1px rgba(0,0,0,.1)}
</style>
</head>
<body>

<!-- Home -->
<section class="screen" style="left:95px;top:53px">
  <div class="status"><span class="signal"><i style="height:2px"></i><i style="height:3px"></i><i style="height:4px"></i><i style="height:5px"></i><i style="height:6px"></i></span><span class="clock">15:23</span><span class="battery">100% <b></b></span></div>
  <div class="menu"><i></i><i></i><i></i></div>
  <div class="brandname" style="top:62px"><span></span>Brindlevale Estates</div>
  <div class="photo" role="img" aria-label="White Mediterranean villa with palm trees, garden steps and a pool" style="left:0;top:99px;width:244px;height:142px"></div>
  <div style="left:0;top:241px;width:244px;height:189px;background:var(--panel)"></div>
  <div class="nav" style="top:263px"><span class="ico"><svg viewBox="0 0 14 14"><circle cx="6" cy="6" r="4" fill="none" stroke="#e0b93a" stroke-width="1.6"/><path d="M9 9l4 4" stroke="#e0b93a" stroke-width="2"/></svg></span><span class="lbl">Search Our Properties</span></div>
  <div class="nav" style="top:293px"><span class="ico"><svg viewBox="0 0 14 14"><circle cx="7" cy="3" r="1.3" fill="#e0b93a"/><rect x="6" y="5.5" width="2" height="6.5" fill="#e0b93a"/></svg></span><span class="lbl">Our Services</span></div>
  <div class="nav" style="top:324px"><span class="ico"><svg viewBox="0 0 14 14"><path d="M7 1L2 6h1.5v4h7V6H12z" fill="#e0b93a"/><path d="M1 9q3 4 6 4t6-4" fill="none" stroke="#e0b93a" stroke-width="1.3"/></svg></span><span class="lbl">Sell your Property with us</span></div>
  <div class="nav active" style="top:355px"><span class="ico"><svg viewBox="0 0 14 14"><rect x="2" y="3" width="9" height="9" fill="none" stroke="#fff" stroke-width="1.2"/><path d="M6 8l6-6" stroke="#fff" stroke-width="1.4"/></svg></span><span class="lbl">Contact</span></div>
  <div class="lang" style="left:47px">Spain</div>
  <div class="lang on" style="left:98px">English</div>
  <div class="lang" style="left:147px">German</div>
</section>

<!-- Sell -->
<section class="screen" style="left:358px;top:53px">
  <div class="status"><span class="signal"><i style="height:2px"></i><i style="height:3px"></i><i style="height:4px"></i><i style="height:5px"></i><i style="height:6px"></i></span><span class="clock">15:23</span><span class="battery">100% <b></b></span></div>
  <div class="menu"><i></i><i></i><i></i></div>
  <div class="badge"><svg viewBox="0 0 28 28"><path d="M14 3L6 11h2.5v7h11v-7H22z" fill="#e0b93a"/><rect x="12" y="13" width="4" height="5" fill="#fff"/><path d="M2 16q5 10 12 10t12-10" fill="none" stroke="#e0b93a" stroke-width="2.4"/></svg></div>
  <div class="heading" style="top:98px">SELL YOUR PROPERTY WITH US</div>
  <p class="copy" style="left:19px;top:117px;width:204px">Coando usted esta considerando la posibilidad de vender su propiedad, siempre puede tratar de vendela usted mismo o puede hacerlo a través de una inmobiliaria profesional, como somos Brindlevale.</p>
  <div class="field" style="left:54px;top:175px;width:134px">Name</div>
  <div class="field" style="left:54px;top:197px;width:134px">Surname</div>
  <div class="field" style="left:54px;top:220px;width:134px">Phone</div>
  <div class="field" style="left:54px;top:242px;width:134px">Email</div>
  <div class="field" style="left:54px;top:265px;width:134px">Property Name</div>
  <div class="bar" style="left:54px;top:286px;width:134px">Property Description</div>
  <div class="area" style="left:54px;top:303px;width:134px;height:64px"></div>
  <div class="btn" style="left:54px;top:395px;width:134px"><svg viewBox="0 0 10 10"><path d="M5 1L1 5h1.3v4h5.4V5H9z" fill="#fff"/></svg>Send us your property</div>
</section>

<!-- Search -->
<section class="screen" style="left:624px;top:53px">
  <div class="status"><span class="signal"><i style="height:2px"></i><i style="height:3px"></i><i style="height:4px"></i><i style="height:5px"></i><i style="height:6px"></i></span><span class="clock">15:23</span><span class="battery">100% <b></b></span></div>
  <div class="menu"><i></i><i></i><i></i></div>
  <div class="badge"><svg viewBox="0 0 28 28"><circle cx="11" cy="11" r="8" fill="none" stroke="#e0b93a" stroke-width="2.6"/><path d="M17 17l8 8" stroke="#e0b93a" stroke-width="3.4" stroke-linecap="round"/><path d="M11 6l-4 4h1.2v4h5.6v-4H15z" fill="#e0b93a"/></svg></div>
  <div class="heading" style="top:98px">SEARCH OUR PROPERTIES</div>
  <div class="bar" style="left:54px;top:118px;width:134px">To Reform</div>
  <div class="area" style="left:54px;top:135px;width:134px;height:28px;font-size:5.8px;color:var(--muted);padding:4px 0 0 7px;line-height:1.9">For Rent<br>To Buy</div>
  <div class="field" style="left:54px;top:184px;width:134px">KEY</div>
  <div class="select" style="left:54px;top:210px;width:134px">TYPE<span class="drop"></span></div>
  <div class="select" style="left:54px;top:234px;width:134px">AREA<span class="drop"></span></div>
  <div class="btn" style="left:54px;top:264px;width:134px"><svg viewBox="0 0 10 10"><circle cx="4" cy="4" r="3" fill="none" stroke="#fff" stroke-width="1.3"/><path d="M6.2 6.2L9 9" stroke="#fff" stroke-width="1.5"/></svg>Search Properties</div>
  <svg style="left:2px;top:370px;width:6px;height:8px" viewBox="0 0 6 8"><path d="M6 0L0 4l6 4z" fill="#e0b93a"/></svg>
  <div class="photo" role="img" aria-label="Villa with pool" style="left:10px;top:338px;width:73px;height:72px"></div>
  <div class="photo" role="img" aria-label="Yellow villa among palm trees" style="left:85px;top:338px;width:73px;height:72px;background:linear-gradient(160deg,#e6f1f8,#5f8f3d 45%,#e9d79b 75%,#6f8f4a)"></div>
  <div class="photo" role="img" aria-label="Townhouses with pine tree" style="left:160px;top:338px;width:73px;height:72px;background:linear-gradient(160deg,#cfe5f5,#4c7a3c 40%,#e8c877 70%,#d8d2c4)"></div>
  <svg style="left:236px;top:370px;width:6px;height:8px" viewBox="0 0 6 8"><path d="M0 0l6 4-6 4z" fill="#e0b93a"/></svg>
</section>

<!-- Contact -->
<section class="screen" style="left:888px;top:53px">
  <div class="status"><span class="signal"><i style="height:2px"></i><i style="height:3px"></i><i style="height:4px"></i><i style="height:5px"></i><i style="height:6px"></i></span><span class="clock">15:23</span><span class="battery">100% <b></b></span></div>
  <div class="menu"><i></i><i></i><i></i></div>
  <div class="badge"><svg viewBox="0 0 28 28"><rect x="5" y="7" width="15" height="16" fill="none" stroke="#e0b93a" stroke-width="2.2"/><path d="M11 17l12-12" stroke="#e0b93a" stroke-width="2.8"/></svg></div>
  <div class="heading" style="top:98px">CONTACT US</div>
  <div class="field" style="left:54px;top:121px;width:136px">Name</div>
  <div class="field" style="left:54px;top:143px;width:136px">Surname</div>
  <div class="field" style="left:54px;top:166px;width:136px">Phone</div>
  <div class="field" style="left:54px;top:188px;width:136px">Email</div>
  <div class="select" style="left:54px;top:210px;width:136px">Property<span class="drop"></span></div>
  <div class="bar" style="left:54px;top:233px;width:136px">Notes</div>
  <div class="area" style="left:54px;top:250px;width:136px;height:64px"></div>
  <div class="btn" style="left:58px;top:331px;width:134px"><svg viewBox="0 0 10 10"><rect x="1" y="2" width="8" height="6" fill="#fff"/><path d="M1 2l4 3 4-3" fill="none" stroke="#1a9ac9" stroke-width=".8"/></svg>Send us your massage</div>
</section>

<!-- Results -->
<section class="screen" style="left:95px;top:510px">
  <div class="status"><span class="signal"><i style="height:2px"></i><i style="height:3px"></i><i style="height:4px"></i><i style="height:5px"></i><i style="height:6px"></i></span><span class="clock">15:23</span><span class="battery">100% <b></b></span></div>
  <div class="menu"><i></i><i></i><i></i></div>
  <p style="left:0;top:44px;width:100%;text-align:center;font-size:8.6px;line-height:1.4;color:var(--ink)">Search results for<br>Key: Beach, tipe, House, Area, Palma</p>

  <div class="photo result-photo" role="img" aria-label="Villa with pool" style="top:89px"></div>
  <div class="result" style="top:108px"><h4>VILLA</h4><p>Traditional Mediterranean villa with partial sea views and close to sandy beaches, shops and restaurants in Cala Egos. With a floor space of 110m2, the house is dis-</p><a>www.brindlevaleestates.com</a></div>

  <div class="photo result-photo" role="img" aria-label="Yellow villa among palm trees" style="top:172px;background:linear-gradient(160deg,#e6f1f8,#5f8f3d 45%,#e9d79b 75%,#6f8f4a)"></div>
  <div class="result" style="top:189px"><h4>VILLA</h4><p>Traditional Mediterranean villa with partial sea views and close to sandy beaches, shops and restaurants in Cala Egos. With a floor space of 110m2, the house is dis-</p><a>www.brindlevaleestates.com</a></div>

  <div class="photo result-photo" role="img" aria-label="Townhouses with pine tree" style="top:255px;background:linear-gradient(160deg,#cfe5f5,#4c7a3c 40%,#e8c877 70%,#d8d2c4)"></div>
  <div class="result" style="top:270px"><h4>VILLA</h4><p>Traditional Mediterranean villa with partial sea views and close to sandy beaches, shops and restaurants in Cala Egos. With a floor space of 110m2, the house is dis-</p><a>www.brindlevaleestates.com</a></div>

  <div class="photo result-photo" role="img" aria-label="Villa terrace with pool and loungers" style="top:338px;background:linear-gradient(160deg,#dbeaf6,#f2efe6 40%,#c9a27a 62%,#3fb3df 85%)"></div>
  <div class="result" style="top:351px"><h4>VILLA</h4><p>Traditional Mediterranean villa with partial sea views and close to sandy beaches, shops and restaurants in Cala Egos. With a floor space of 110m2, the house is dis-</p><a>www.brindlevaleestates.com</a></div>
</section>

<!-- Property detail -->
<section class="screen" style="left:358px;top:510px">
  <div class="status"><span class="signal"><i style="height:2px"></i><i style="height:3px"></i><i style="height:4px"></i><i style="height:5px"></i><i style="height:6px"></i></span><span class="clock">15:23</span><span class="battery">100% <b></b></span></div>
  <div class="menu"><i></i><i></i><i></i></div>
  <div class="heading" style="top:54px;color:var(--gold)">VILLA BRINDLEVALE</div>
  <div class="photo" role="img" aria-label="White villa with terracotta roof, garden and pool" style="left:0;top:58px;width:244px;height:182px;top:72px;height:168px"></div>
  <div class="copy" style="left:17px;top:254px;width:210px;font-size:6.5px;text-align:left">
    <p>Traditional Mediterranean villa with partial sea views and close to sandy beaches, shops and restaurants in Cala Egos.</p>
    <p style="margin-top:14px">With a floor space of 110m2, the house is distributed over 2 floors as follows:<br>On the ground floor we find a cozy living room with fireplace, fully equipped kitchen and 2 double bedrooms with 1 bathroom.<br>On the upper floor there is 1 bedroom with bathroom. From the bedroom we have access to a terrace from which we can enjoy a fantastic view of the sea.</p>
    <p style="margin-top:9px">The house offers air conditioning in all rooms, barbecue and large terraces with 2 terraces.</p>
  </div>
  <div class="btn" style="left:54px;top:399px;width:135px"><svg viewBox="0 0 10 10"><rect x="1" y="2" width="8" height="6" fill="#fff"/><path d="M1 2l4 3 4-3" fill="none" stroke="#1a9ac9" stroke-width=".8"/></svg>Send Request Information</div>
</section>

<!-- Services -->
<section class="screen" style="left:624px;top:510px">
  <div class="status"><span class="signal"><i style="height:2px"></i><i style="height:3px"></i><i style="height:4px"></i><i style="height:5px"></i><i style="height:6px"></i></span><span class="clock">15:23</span><span class="battery">100% <b></b></span></div>
  <div class="menu"><i></i><i></i><i></i></div>
  <div class="badge"><svg viewBox="0 0 28 28"><circle cx="14" cy="5" r="3" fill="#e0b93a"/><path d="M10 10h6v12h3v3H9v-3h3v-9h-2z" fill="#e0b93a"/></svg></div>
  <div class="heading" style="top:98px">Our Services</div>
  <p class="copy" style="left:19px;top:122px;width:206px;text-align:left">Cala d'Or es un sitio emblemático de la costa del levante mallorquin. Esta zona costera y sus alrededores son uno de los primers lugares turisticos de Malloca y se encuetran a tan solo 45 minutos del aeropuerto y de la favulosa capital de Palma.</p>
  <div class="service" style="top:194px">SEGUROS</div>
  <div class="service" style="top:219px">COMPRA</div>
  <div class="service" style="top:246px">MANTENIMIENTOS</div>
  <div class="service" style="top:271px">OBRAS Y REFORMAS</div>
  <div class="brandname" style="top:350px"><span></span>Brindlevale Estates</div>
</section>

</body>
</html>
```